Coach needs thank you cards (business card format) to deliver to customers. Model behavior

I am a coach who needs thank-you cards for customers and people to appreciate "exemplary behavior". First and foremost it is about the mindfulness of the people who have a great behavior to estimate and reward. The colors should contain silver and light like the logo of Mentorbrightpath.
Updates

The following should include the cards front and back. Front: Praise for: there should be room below to enter the name of the person. The fangs should be silver and light blue as on the logo which I have uploaded. Back: capitalized by date: exemplary behavior should be at the bottom right. mentorbrightpath.ch

```html
<!DOCTYPE html>
<html lang="de">
<head>
<meta charset="utf-8">
<title>Mentorbrightpath – Lobkarte</title>
<link href="https://fonts.googleapis.com/css2?family=Michroma&display=swap" rel="stylesheet">
<style>
  :root {
    --backdrop: #e6e7e7;
    --brand-blue: #2c74b9;
    --silver-blue: #a9c6e8;
    --ink-blue: #2f74b8;
    --paper: #ffffff;
  }
  * { box-sizing: border-box; margin: 0; padding: 0; }
  html, body {
    width: 1200px; height: 1200px; overflow: hidden;
    background: var(--backdrop);
    font-family: "Michroma", sans-serif;
  }
  .card {
    position: absolute;
    top: 277px;
    width: 364px;
    height: 637px;
    overflow: hidden;
  }
  .card--front { left: 184px; background: var(--brand-blue); }
  .card--back  { left: 652px; background: var(--paper); }

  .card p, .card span { line-height: 1; white-space: nowrap; }

  .front-brand {
    position: absolute;
    top: 196px; left: 0; right: 0;
    display: flex; flex-direction: column; align-items: center;
    color: var(--silver-blue);
  }
  .front-brand__circle {
    width: 52px; height: 52px;
    border: 2px solid var(--silver-blue);
    border-radius: 50%;
  }
  .front-brand__name {
    margin-top: 7px;
    font-size: 7.5px;
    letter-spacing: 1.5px;
  }
  .front-title {
    position: absolute;
    top: 275px; left: 0; right: 0;
    text-align: center;
    color: var(--silver-blue);
    font-size: 16px;
    letter-spacing: 2px;
  }

  .back-date {
    position: absolute;
    top: 268px; left: 0; right: 0;
    text-align: center;
    color: var(--ink-blue);
    font-size: 13.5px;
    letter-spacing: 3px;
  }
  .back-title {
    position: absolute;
    top: 302px; left: 0; right: 0;
    text-align: center;
    color: var(--ink-blue);
    font-size: 20px;
    font-variant: small-caps;
    letter-spacing: 0.5px;
  }
  .back-url {
    position: absolute;
    top: 616px; left: 0; right: 0;
    text-align: center;
    color: var(--ink-blue);
    font-size: 12.5px;
    letter-spacing: 1px;
  }
</style>
</head>
<body>
  <section class="card card--front">
    <div class="front-brand">
      <span class="front-brand__circle"></span>
      <span class="front-brand__name">MENTORBRIGHTPATH</span>
    </div>
    <p class="front-title">EIN LOB FÜR</p>
  </section>

  <section class="card card--back">
    <p class="back-date">20.01.2018</p>
    <p class="back-title">Vorbildliches Verhalten</p>
    <p class="back-url">MENTORBRIGHTPATH.CH</p>
  </section>
</body>
</html>
```